I need a book cover for my book titled Sunny Porch! The subtitle is Quiet Orchard Days and the the author is Marisol Dunleavy. I want the attached photo included on the cover, plus the words "I never met a chicken wing I didn't like!" The book size is 5.06 x 7.81 in. and is 146 pages. For the color scheme, I like a chocolate brown cover with aqua blue letters. (Please note that you don't have to use these colors. Feel free to use this color scheme or whatever you colors you like!)

• Please include my photo for the back cover, along with this text:

Sunny Porch! I was tired of being tired! I was tired of acid reflux, body stiffness, and being overweight. To make matters worse, I suffered from back pain, constipation, leg pain, and lack of sleep. If you are tired of looking to medical test for your answers, this is the book for you. The key was the day I decided to make “me” a priority by being #1 on my “to-do” list.

Our healthcare system seems to be more concerned about treating illness than they are about preventing it; which is why we have so many problems with our health and wellness. That’s why I’m going to give you insights into nutrition, health care, and the pharmaceutical industry.

I’m also going to give you some insights into exercise, supplements, detoxing and essential oils; as well as what goes into your grocery cart and the foods you feed your family.

Because you’re reading this I know you’re ready to live your best life, Sunny Porch! is for you.

Here’s to a healthy you!

Here's a brief bio about the author for the back cover:

Marisol lives in Chicago with her husband, Dr. Wendell, and has three adult children. She is probably one of the most private people you will meet – BUT HAD to tell her story!

```html
<!DOCTYPE html>
<html lang="en">
<head>
<meta charset="utf-8">
<title>Sunny Porch! Quiet Orchard Days — Book Cover</title>
<link rel="stylesheet" href="https://fonts.googleapis.com/css2?family=Bebas+Neue&family=Della+Respira&display=swap">
<style>
  :root {
    --brown-deep: #3f2318;
    --brown: #4d2c1f;
    --brown-light: #5e3a2a;
    --aqua: #3cb9c2;
    --aqua-light: #6fd6dc;
    --aqua-dark: #1e8f98;
    --cream: #f4ede6;
    --white: #ffffff;
  }
  * { margin: 0; padding: 0; box-sizing: border-box; }
  html, body { width: 1200px; height: 894px; overflow: hidden; background: var(--brown-deep); }
  .cover {
    position: relative;
    width: 1200px;
    height: 894px;
    background:
      radial-gradient(ellipse at 85% 85%, var(--brown-light) 0%, transparent 55%),
      linear-gradient(180deg, var(--brown) 0%, var(--brown-deep) 100%);
    overflow: hidden;
    font-family: "Della Respira", Georgia, serif;
    color: var(--cream);
  }

  /* Back cover */
  .back-blurb {
    position: absolute;
    left: 36px;
    top: 46px;
    width: 528px;
    text-align: center;
    font-size: 15.6px;
    line-height: 27.4px;
  }
  .back-blurb p + p { margin-top: 27px; }
  .back-portrait {
    position: absolute;
    left: 40px;
    top: 538px;
    width: 116px;
    height: 147px;
    border: 2px solid var(--cream);
    background: linear-gradient(160deg, #a9743e 0%, #6a3f22 60%, #3a2216 100%);
  }
  .back-toast {
    position: absolute;
    left: 196px;
    top: 524px;
    width: 180px;
    text-align: center;
    font-size: 15.6px;
  }
  .author-bio {
    position: absolute;
    left: 40px;
    top: 689px;
    width: 536px;
    text-align: center;
    font-size: 15.2px;
    line-height: 25px;
    color: var(--aqua);
  }

  /* Spine */
  .spine-title {
    position: absolute;
    left: 612px;
    top: 46px;
    transform-origin: 0 0;
    transform: rotate(90deg);
    white-space: nowrap;
    font-family: "Bebas Neue", "Arial Narrow", sans-serif;
    font-size: 28px;
    letter-spacing: 0.5px;
    color: var(--white);
  }
  .spine-title .accent { color: var(--aqua); }
  .spine-author {
    position: absolute;
    left: 614px;
    top: 762px;
    transform-origin: 0 0;
    transform: rotate(90deg);
    white-space: nowrap;
    font-size: 22px;
    color: var(--white);
  }

  /* Front cover */
  .front-title {
    position: absolute;
    left: 640px;
    top: 0;
    width: 545px;
    height: 240px;
    font-family: "Bebas Neue", "Arial Narrow", sans-serif;
    font-weight: 400;
    line-height: 1;
    white-space: nowrap;
  }
  .front-title .title-main {
    position: absolute;
    left: 0;
    right: 0;
    top: 32px;
    text-align: center;
    font-size: 118px;
    letter-spacing: 1px;
    color: var(--aqua);
  }
  .front-title .title-sub {
    position: absolute;
    left: 0;
    right: 0;
    top: 160px;
    text-align: center;
    font-size: 72px;
    letter-spacing: 1px;
    background: linear-gradient(180deg, var(--aqua-light) 0%, var(--aqua) 50%, var(--aqua-dark) 100%);
    -webkit-background-clip: text;
    background-clip: text;
    color: transparent;
  }
  .tagline {
    position: absolute;
    left: 640px;
    top: 258px;
    width: 545px;
    text-align: center;
    white-space: nowrap;
    font-size: 28px;
    color: var(--aqua);
  }
  .wing-platter {
    position: absolute;
    left: 660px;
    top: 322px;
    width: 512px;
    height: 344px;
  }
  .front-portrait {
    position: absolute;
    left: 620px;
    top: 658px;
    width: 186px;
    height: 236px;
    border: 2px solid var(--aqua);
    background: linear-gradient(160deg, #a9743e 0%, #6a3f22 60%, #3a2216 100%);
  }
  .front-author {
    position: absolute;
    left: 866px;
    top: 824px;
    font-size: 25px;
    color: var(--aqua);
  }
</style>
</head>
<body>
<main class="cover">

  <section class="back-cover">
    <div class="back-blurb">
      <p>Sunny Porch! I was tired of being tired! I was tired of acid reflux, body stiffness, and being overweight. To make matters worse, I suffered from back pain, constipation, leg pain, and lack of sleep. If you are tired of looking to medical test for your answers, this is the book for you. The key was the day I decided to make “me” a priority by being #1 on my “to-do” list.</p>
      <p>Our healthcare system seems to be more concerned about treating illness than they are about preventing it; which is why we have so many problems with our health and wellness. That’s why I’m going to give you insights into nutrition, health care, and the pharmaceutical industry.</p>
      <p>I’m also going to give you some insights into exercise, supplements, detoxing and essential oils; as well as what goes into your grocery cart and the foods you feed your family.</p>
      <p>Because you’re reading this I know you’re ready to live your best life, Sunny Porch! is for you.</p>
    </div>
    <div class="back-portrait" role="img" aria-label="Author portrait photo"></div>
    <p class="back-toast">Here’s to a healthy you!</p>
    <p class="author-bio">“Marisol lives in Chicago with her husband, Dr. Wendell, and has three adult children. She is probably one of the most private people you will meet – BUT HAD to tell her story!”</p>
  </section>

  <section class="spine">
    <div class="spine-title">Sunny Porch<span class="accent">!</span> Quiet Orchard Days</div>
    <div class="spine-author">Marisol</div>
  </section>

  <section class="front-cover">
    <h1 class="front-title">
      <span class="title-main">Sunny Porch!</span>
      <span class="title-sub">Quiet Orchard Days</span>
    </h1>
    <p class="tagline">I never met a chicken wing I didn't like!</p>
    <svg class="wing-platter" viewBox="0 0 512 344" role="img" aria-label="Photo of glazed chicken wings with celery, carrots and dip on a white warning-labelled tray">
      <defs>
        <radialGradient id="platterTone" cx="50%" cy="50%" r="50%">
          <stop offset="0%" stop-color="#b8452a"/>
          <stop offset="45%" stop-color="#c9785f"/>
          <stop offset="75%" stop-color="#e4dcd6"/>
          <stop offset="100%" stop-color="#e4dcd6" stop-opacity="0"/>
        </radialGradient>
      </defs>
      <ellipse cx="256" cy="180" rx="250" ry="160" fill="url(#platterTone)"/>
    </svg>
    <div class="front-portrait" role="img" aria-label="Author portrait photo"></div>
    <p class="front-author">Marisol</p>
  </section>

</main>
</body>
</html>
```